TRIVEX-PRO Web Design

We are a Health, Safety, Environmental & Quality Recruitment Agency, our clients are major corporate Mining, Oil & Gas and Engineering companies. We have offices in Perth & Melbourne, Australia

The website should be very functional & easy to navigate

BUT REALLY LOOKING FOR WOW FACTOR!
Updates

Please Note: TRIVEX HOLDINGS IS OUR OLD COMPANY THE NEW ONE IS "TRIVEX-PRO" 

Some idea's from our competitors:

http://www.guardlinemerit.com.au/
http://www.wardenplacement.com.au/
http://www.keelhunt.com.au/
http://www.brqstaffing.co.uk/
http://www.laborvane.com/health-safety-environment-jobs

Would love to see some of our valued clients and there logos

still looking for wow factor

Industry/Entity Type

Mining

Requirements
Must have
• A place where candidates can upload there resumes & other contact details
• eg: http://www.guardlinemerit.com.au/candidates/register-your-resume/
• A place we can load jobs on to eg: http://www.guardlinemerit.com.au/vacancies/
• Contact details:
• Perth: 17 Brindlecombe Ave, West Perth, Western Australia 6005
• t: 08 9517 3064 | f: 08 9517 3070 |
• Melbourne: Level 1, 212 Harrowgate Street, Melbourne, Victoria 3000
• t: 03 9655 4217| f: 03 9655 4290 |
• e: dmorl@trivexpro.com.au | w: http://www.trivexpro.com.au

```html
<!DOCTYPE html>
<html lang="en">
<head>
<meta charset="utf-8">
<title>trivexpro — Resources Recruitment</title>
<link href="https://fonts.googleapis.com/css2?family=Roboto+Condensed:wght@300;400;700&family=Open+Sans:ital,wght@0,400;0,600;0,700;1,400;1,600&display=swap" rel="stylesheet">
<style>
:root{
  --blue:#2e87bd;
  --ink:#333;
  --text:#666;
  --grey-bar:#555;
  --footer:#f0f0f0;
  --line:#d6d6d6;
  --gold:#f7b500;
}
*{box-sizing:border-box;margin:0;padding:0}
html,body{width:912px;height:1200px;overflow:hidden;background:#fff}
body{position:relative;font-family:"Open Sans",sans-serif;color:var(--text)}
.abs{position:absolute}
.header{left:0;top:0;width:912px;height:105px;background:linear-gradient(#fafafa,#f3f4f5)}
.brand-mark{left:96px;top:12px;width:76px;height:76px;background:var(--blue);border-radius:4px}
.brand-name{left:188px;top:30px;font-family:"Roboto Condensed",sans-serif;font-weight:300;font-size:34px;color:var(--blue);letter-spacing:1px}
.phone{left:645px;top:19px;display:flex;align-items:center;gap:6px;font:italic 700 16px "Open Sans",sans-serif;color:var(--blue)}
.nav a{position:absolute;top:54px;height:27px;line-height:25px;font-family:"Roboto Condensed",sans-serif;font-size:12.5px;color:#555;text-decoration:none;white-space:nowrap}
.nav a.active{left:373px;width:52px;text-align:center;border:1px solid var(--blue);border-top-width:2px;color:var(--blue)}
.hero{left:0;top:105px;width:912px;height:270px;background:linear-gradient(90deg,#6b4a2a 0%,#c98a3a 30%,#3e4a63 55%,#8a5b25 75%,#e59a2a 100%)}
.hero-title{left:507px;top:131px;font-family:"Roboto Condensed",sans-serif;font-weight:400;font-size:18.5px;color:var(--gold);text-shadow:0 1px 2px rgba(0,0,0,.5);white-space:nowrap}
.hero-text{left:507px;top:156px;width:305px;font-weight:700;font-size:12px;line-height:18px;color:#fff;text-shadow:0 1px 2px rgba(0,0,0,.5)}
.card{top:397px;width:224px;height:147px}
.card .photo{height:119px;background:linear-gradient(#d8d8d8,#9a9a9a)}
.card .label{height:28px;line-height:30px;text-align:center;color:#fff;font-family:"Roboto Condensed",sans-serif;font-size:15px;background:var(--grey-bar)}
.card.featured .photo{background:linear-gradient(#c9d6e2,#5f7690)}
.card.featured .label{background:var(--blue)}
.plus{left:193px;top:494px;width:28px;height:28px;border-radius:50%;background:var(--blue);color:#fff;font:700 20px/27px "Open Sans",sans-serif;text-align:center}
.welcome{left:95px;top:561px;width:520px}
.welcome h2{font-family:"Roboto Condensed",sans-serif;font-weight:400;font-size:22px;color:var(--ink);padding-bottom:6px;border-bottom:2px dotted #bbb}
.welcome h2 span{color:var(--blue)}
.welcome p{font-size:9.6px;line-height:16px;margin-top:6px;text-align:justify}
.finder{left:642px;top:565px;width:175px;height:200px;border:1px solid var(--line)}
.finder .head{height:31px;background:var(--blue);color:#fff;font-family:"Roboto Condensed",sans-serif;font-size:18px;line-height:31px;padding-left:12px;position:relative}
.field{margin:8px 10px 0;height:24px;border:1px solid #ccc;font:italic 8.5px/22px "Open Sans",sans-serif;color:#999;padding-left:6px;position:relative}
.field .arrow{position:absolute;right:2px;top:2px;width:18px;height:18px;background:var(--blue)}
.submit{position:absolute;right:10px;bottom:10px;width:60px;height:21px;background:var(--blue);color:#fff;font:italic 700 11px/21px "Open Sans",sans-serif;text-align:center}
.tabs{left:95px;top:780px;display:flex}
.tab{height:25px;line-height:25px;padding:0 20px 0 14px;color:#fff;font-family:"Roboto Condensed",sans-serif;font-size:14px;background:var(--grey-bar);clip-path:polygon(0 0,88% 0,100% 100%,0 100%);margin-right:-8px}
.tab.active{background:var(--blue)}
.jobs{left:95px;top:805px;width:346px;height:141px;border:1px solid var(--line)}
.job{display:flex;gap:10px;padding:11px 10px;border-bottom:1px solid var(--line);height:62px}
.date{width:60px;height:38px;border:1px solid #ccc;display:flex;box-shadow:2px 2px 0 #e5e5e5;flex:none}
.date .day{width:24px;background:var(--blue);color:#fff;font:700 15px/36px "Open Sans",sans-serif;text-align:center}
.date .my{font:italic 600 10px/13px "Open Sans",sans-serif;color:var(--blue);padding:4px 0 0 6px}
.job h4{font-size:11px;color:var(--blue);font-weight:700}
.job p{font-size:9.3px;line-height:14px;color:#555}
.job b{color:var(--blue);font-weight:600}
.more{position:absolute;font:italic 600 11px "Open Sans",sans-serif;color:var(--blue)}
.testi-head{left:716px;top:778px;font-family:"Roboto Condensed",sans-serif;font-size:19px;color:var(--blue)}
.testi{left:493px;top:796px;width:324px;height:150px;border:1px solid var(--line);box-shadow:0 3px 0 #e6eaee}
.testi-photo{left:481px;top:798px;width:104px;height:72px;background:linear-gradient(#c7d3dd,#6f7f8e);border:4px solid #fff;box-shadow:0 1px 4px rgba(0,0,0,.35);transform:rotate(-1deg)}
.testi p{position:absolute;left:105px;top:8px;width:212px;font-size:9.4px;line-height:17.5px}
.testi .name{position:absolute;left:10px;top:80px;font:italic 600 9.5px "Open Sans",sans-serif;color:var(--blue)}
.footer{left:0;top:975px;width:912px;height:190px;background:var(--footer)}
.col{top:987px}
.col h5{font-family:"Roboto Condensed",sans-serif;font-weight:400;font-size:13px;color:var(--blue);margin-bottom:6px}
.col li{list-style:none;font-size:9.6px;line-height:18.1px;color:#444}
.col li::before{content:"» ";font-size:8px;color:#888}
.socials{display:flex;gap:4px;margin:4px 0 14px}
.socials span{width:18px;height:18px;background:#555}
.office{font-size:9.6px;line-height:13.5px;color:#444}
.office em{font-style:normal;color:var(--blue)}
.locate{margin-top:6px;width:135px;height:20px;background:var(--blue);color:#fff;font-family:"Roboto Condensed",sans-serif;font-size:12.5px;line-height:20px;padding-left:35px;position:relative}
.copy{left:0;top:1176px;width:912px;text-align:center;font-size:8.5px;color:#444}
</style>
</head>
<body>
<div class="abs header"></div>
<div class="abs brand-mark"></div>
<div class="abs brand-name">trivexpro</div>
<div class="abs phone">
  <svg width="20" height="20" viewBox="0 0 24 24"><path fill="#555" d="M6.6 10.8c1.4 2.8 3.8 5.1 6.6 6.6l2.2-2.2c.3-.3.7-.4 1-.2 1.1.4 2.3.6 3.6.6.6 0 1 .4 1 1V20c0 .6-.4 1-1 1C10.6 21 3 13.4 3 4c0-.6.4-1 1-1h3.5c.6 0 1 .4 1 1 0 1.2.2 2.4.6 3.6.1.3 0 .7-.2 1z"/></svg>
  61 (08) 9517 3064
</div>
<nav class="nav">
  <a class="active" href="#">Home</a>
  <a href="#" style="left:437px">About Us</a>
  <a href="#" style="left:503px">Positions We Offer</a>
  <a href="#" style="left:609px">Candidates</a>
  <a href="#" style="left:684px">Employers</a>
  <a href="#" style="left:755px">Contact Us</a>
</nav>

<div class="abs hero" role="img" aria-label="Two smiling site workers in hard hats and safety gear at an industrial plant"></div>
<h1 class="abs hero-title">FOCUSING ON THE RESOURCES INDUSTRY</h1>
<p class="abs hero-text">Lorem ipsum dolor sit amet, consectetur adipiscing elit. Morbi a luctus risus. Nam tempor pulvinar ligula nec tempor. Cras diam purus, condimentum sed tempus id.</p>

<div class="abs card featured" style="left:95px"><div class="photo" role="img" aria-label="Team of business professionals"></div><div class="label">Positions We Offer</div></div>
<div class="abs plus">+</div>
<div class="abs card" style="left:344px"><div class="photo" role="img" aria-label="Business handshake in black and white"></div><div class="label">Candidates</div></div>
<div class="abs card" style="left:593px"><div class="photo" role="img" aria-label="Business people in a city setting, black and white"></div><div class="label">Employers</div></div>

<section class="abs welcome">
  <h2>Welcome to <span>trivexpro</span></h2>
  <p>Lorem ipsum dolor sit amet, consectetur adipiscing elit. Nam eget elit lacinia sapien aliquam congue in sed nulla. Sed id tellus placerat, pulvinar justo vitae, pulvinar urna. Aliquam fringilla elit bibendum, adipiscing arcu non, tristique neque. Sed in ante magna. Maecenas facilisis luctus vulputate. Aliquam feugiat varius massa, a facilisis diam consectetur ut. Maecenas hendrerit congue dolor, sagittis posuere nulla tincidunt ac. Nam porttitor velit id nulla porta auctor. Maecenas quis odio in risus bibendum placerat ut eget velit. Phasellus condimentum metus lorem, sed tincidunt felis tincidunt vitae. Fusce ultricies lectus et nulla ornare, mattis suscipit nulla venenatis.</p>
  <p>Aenean risus risus, facilisis a iaculis a, hendrerit at lectus. Proin suscipit neque in justo volutpat, nec auctor nunc vestibulum. Mauris consectetur vestibulum purus, sit amet sagittis nulla imperdiet mattis. Cum sociis natoque penatibus et magnis dis parturient montes, nascetur ridiculus mus. Sed suscipit purus velit, a accumsan tellus commodo at. Fusce quis ante eu justo aliquam bibendum nec at orci. Ut mauris tellus, dignissim et tempor vel.</p>
</section>

<aside class="abs finder">
  <div class="head">Find a Job
    <svg style="position:absolute;right:8px;top:3px" width="26" height="26" viewBox="0 0 26 26"><circle cx="13" cy="13" r="11" fill="none" stroke="#fff" stroke-width="1.5"/><circle cx="13" cy="10" r="3.5" fill="#fff"/><path d="M7 20c1-4 3-5 6-5s5 1 6 5z" fill="#fff"/></svg>
  </div>
  <div class="field" style="margin-top:11px">Keywords</div>
  <div class="field">All Classifications<span class="arrow"></span></div>
  <div class="field">Select a Classifications fist<span class="arrow"></span></div>
  <div class="field">All location<span class="arrow"></span></div>
  <div class="submit">Submit</div>
</aside>

<div class="abs tabs"><div class="tab active">Latest Jobs</div><div class="tab">Browse Area</div><div class="tab">Latest Blog</div></div>
<div class="abs jobs">
  <div class="job"><div class="date"><div class="day">02</div><div class="my">Jan<br>2013</div></div><div><h4>Lorem ipsum dolor sit amet</h4><p><b>Time:</b> 6:00 PM / <b>Location:</b> Australia</p><p>orem ipsum dolor sit amet consectetur adipiscing elit sed</p></div></div>
  <div class="job"><div class="date"><div class="day">15</div><div class="my">Feb<br>2013</div></div><div><h4>Lorem ipsum dolor sit amet</h4><p><b>Time:</b> 6:00 PM / <b>Location:</b> Australia</p><p>orem ipsum dolor sit amet consectetur adipiscing elit sed</p></div></div>
  <span class="more" style="right:14px;bottom:6px">More »</span>
</div>

<div class="abs testi-head">Testimonials</div>
<div class="abs testi">
  <p>Lorem ipsum dolor sit amet, consectetur adipiscing elit. Sed varius fringilla urna, vitae imperdiet sem. Fusce consectetur commodo aliquet. In faucibus dui risus, eu ultricies tellus elementum in. Phasellus dignissim eget ipsum in egestas.</p>
  <span class="name">Employee name</span>
  <span class="more" style="right:12px;bottom:8px">More »</span>
</div>
<div class="abs testi-photo" role="img" aria-label="Portrait of a smiling employee"></div>

<footer class="abs footer"></footer>
<div class="abs col" style="left:95px"><h5>Job Seekers</h5><ul><li>Find a Job</li><li>Candidate Portal</li><li>Login</li><li>Register with Us</li><li>Areas of Expertise</li><li>Learn New Skills</li><li>Resource Library</li><li>Our Partnerships</li></ul></div>
<div class="abs col" style="left:267px"><h5>Employers</h5><ul><li>Areas of Expertise</li><li>Risk Mitgation</li><li>Services &amp; Solutions</li><li>Our Differentiators</li><li>A Secure Business Partner</li><li>Client Credit Application</li></ul></div>
<div class="abs col" style="left:475px"><h5>Candidates</h5><ul><li>Fast Facts</li><li>Vision, Mission &amp; Values</li><li>CEO Message</li><li>Our Board</li><li>Senior Management Team</li><li>Social Responsibility</li><li>Awards &amp; Recognition</li><li>Our Policies</li></ul></div>
<div class="abs col" style="left:682px">
  <h5>Follow us</h5>
  <div class="socials"><span></span><span></span><span></span><span></span><span></span></div>
  <h5 style="margin-bottom:2px">Perth Office</h5>
  <div class="office">Suite 4, 96 Corrimal Street Subiaco<br>Western Australia 6008<br><em>Phone:</em> +61 (08) 9517 3064<br><em>Email:</em> perth@trivexpro.com.au</div>
  <div class="locate">
    <svg style="position:absolute;left:4px;top:-4px" width="24" height="26" viewBox="0 0 24 26"><path d="M12 1a7 7 0 0 0-7 7c0 5 7 12 7 12s7-7 7-12a7 7 0 0 0-7-7z" fill="#fff" stroke="#2e87bd" stroke-width="1.5"/><circle cx="12" cy="8" r="2.5" fill="#2e87bd"/></svg>
    Find More Location
  </div>
</div>
<div class="abs copy">© 2012-2013 trivexpro. All Rights Reserved</div>
</body>
</html>
```